Business Card Design Project

We need a business card design for a relatively new company called Velmar Gear. We design paddle (an outdoor winter sport primarily played in the midwest and east coast) and tennis bags for women and men. Velmar Gear is a lifestyle brand for the next generation country club goers. Our bags merge fashion with functionality and are making country club sports trendier and more fashionable.

I would like to include space for
Name: (will fill this in for employees)
Velmar Gear
Phone: (will do this)
Email:
www.velmargear.example

Would also like to include Chatterbook and Flitter icons.
Please do not use pictures of the bags - this is just to give you an idea of what style bags we sell.

Target Market(s)

30 to 40 year old men and women - luxury market

Industry/Entity Type

Fashion

Requirements
Must have
• Would like the company logo included

```html
<!DOCTYPE html>
<html lang="en">
<head>
<meta charset="utf-8">
<title>Velmar Gear – Business Card</title>
<link rel="stylesheet" href="https://fonts.googleapis.com/css2?family=Questrial&family=Arimo:wght@400;700&display=swap">
<style>
  :root {
    --bg: #e9e6e1;
    --card: #ffffff;
    --ink: #1f1f1f;
    --ink-soft: #333333;
    --rule: #3a3a3a;
    --shadow: rgba(0, 0, 0, 0.18);
  }
  * { box-sizing: border-box; margin: 0; padding: 0; }
  html, body {
    width: 1200px; height: 754px; overflow: hidden;
    background: var(--bg);
  }
  .stage {
    position: relative; width: 1200px; height: 754px;
  }
  .card {
    position: absolute; top: 217px;
    width: 540px; height: 320px;
    background: var(--card);
    box-shadow: 0 6px 18px var(--shadow);
  }
  .card--front { left: 40px; }
  .card--back { left: 620px; }

  /* Front */
  .brand {
    position: absolute; left: 52px; top: 56px;
    display: flex; align-items: center; gap: 18px;
  }
  .brand__dot {
    width: 52px; height: 52px; border-radius: 50%;
    background: var(--ink);
  }
  .brand__name {
    font-family: "Questrial", sans-serif;
    font-size: 54px; color: var(--ink); letter-spacing: 1px;
  }
  .person {
    position: absolute; left: 80px; top: 210px;
    font-family: "Arimo", sans-serif; color: var(--ink);
  }
  .person__name { font-size: 21px; font-weight: 700; }
  .person__title { font-size: 15px; margin-top: 3px; color: var(--ink-soft); }
  .divider {
    position: absolute; left: 300px; top: 168px;
    width: 1px; height: 152px; background: var(--rule);
  }
  .contacts {
    position: absolute; left: 316px; top: 178px;
    list-style: none;
    font-family: "Arimo", sans-serif; font-size: 14px; color: var(--ink);
  }
  .contacts li {
    display: flex; align-items: center; gap: 7px; height: 24px;
  }
  .contacts svg { width: 13px; height: 13px; flex: none; }
  .contacts .social-mark {
    width: 11px; height: 11px; background: var(--ink-soft); flex: none;
  }

  /* Back */
  .back-mark {
    position: absolute; left: 0; right: 0; top: 70px;
    display: flex; flex-direction: column; align-items: center; gap: 18px;
  }
  .back-mark__dot {
    width: 90px; height: 90px; border-radius: 50%; background: var(--ink);
  }
  .back-mark__name {
    font-family: "Questrial", sans-serif; font-size: 40px; color: var(--ink);
  }
  .back-url {
    position: absolute; left: 0; right: 0; bottom: 36px; text-align: center;
    font-family: "Arimo", sans-serif; font-size: 17px;
    letter-spacing: 6px; color: var(--ink);
  }
</style>
</head>
<body>
<main class="stage">
  <section class="card card--front">
    <div class="brand">
      <span class="brand__dot"></span>
      <span class="brand__name">Velmar Gear</span>
    </div>
    <div class="person">
      <p class="person__name">Full Name</p>
      <p class="person__title">Title</p>
    </div>
    <div class="divider"></div>
    <ul class="contacts">
      <li>
        <svg viewBox="0 0 16 16" aria-hidden="true"><path d="M4 1.5l2.5 3-1.5 1.5c.8 2 2.5 3.7 4.5 4.5l1.5-1.5 3 2.5-1.5 2.5C7 14 2 9 1.5 3z" fill="#1f1f1f"/></svg>
        <span>012-555-0147</span>
      </li>
      <li>
        <svg viewBox="0 0 16 16" aria-hidden="true"><rect x="1" y="3" width="14" height="10" fill="none" stroke="#1f1f1f" stroke-width="1.6"/><path d="M1 3l7 6 7-6" fill="none" stroke="#1f1f1f" stroke-width="1.6"/></svg>
        <span>info@velmargear.example</span>
      </li>
      <li>
        <svg viewBox="0 0 16 16" aria-hidden="true"><circle cx="8" cy="8" r="6.5" fill="none" stroke="#1f1f1f" stroke-width="1.4"/><ellipse cx="8" cy="8" rx="3" ry="6.5" fill="none" stroke="#1f1f1f" stroke-width="1.2"/><path d="M1.5 8h13" stroke="#1f1f1f" stroke-width="1.2"/></svg>
        <span>www.velmargear.example</span>
      </li>
      <li><span class="social-mark"></span><span>Chatterbook @velmargear</span></li>
      <li><span class="social-mark"></span><span>Flitter @velmargear</span></li>
    </ul>
  </section>

  <section class="card card--back">
    <div class="back-mark">
      <span class="back-mark__dot"></span>
      <span class="back-mark__name">Velmar Gear</span>
    </div>
    <p class="back-url">www.velmargear.example</p>
  </section>
</main>
</body>
</html>
```